Pawsome Trails business card

I need a business card design for a dog training company in Toronto called Pawsome Trails. My training is unique, outdoor training that helps people create a better bond with their dog through communication and understanding their dog's true nature. I do not use treats - but communication and praise for the dog.

I help people create a better life for them and their dog. From puppy training right through to seniors, I offer both group classes called Curbside Calm Program as well as in-home private sessions.

I believe that having a dog is a lifestyle, so I encourage clients to incorporate their dog into their active life. Outdoor activities such as hiking, mental stimulation, proper care and healthy food for their dog are all keys to a healthy and happy dog.

I would like a fresh and modern look that works with my logo. I would like to convey fun, confidence and happiness.

My services are premium services. I am a Certified Dog Trainer, and offer value for money, but my prices are higher than other trainers.
Updates

Thank you to everyone who submitted designs! I'm so impressed with the level of creativity and the options that you all have given me. It will be a difficult choice for sure. As this was my first experience with Sketch Bazaar - it has been a great one.

marla.

Industry/Entity Type

Communication

Requirements
Must have
• Marla Quinby, CTE
Certified Trainer Educator
marla@pawsometrails.ca
647-555-0183
pawsometrails.ca

Prefer a double sided card.
Must have Pawsome Trails logo. File attached. I do have a stroke logo for a dark background as well.

Must only use the fonts and colours as outlined in my brand guidelines, which are attached.
Should not have
• no cheesy pet images
do not use the tongue as an element outside of the logo
minimize the use of pink - can be used as an accent colour but should not be a main colour

```html
<!DOCTYPE html>
<html lang="en">
<head>
<meta charset="utf-8">
<title>Pawsome Trails – Business Card</title>
<link rel="stylesheet" href="https://fonts.googleapis.com/css2?family=Arimo:wght@400;700&display=swap">
<style>
  :root {
    --bg-centre: #f4f6f6;
    --bg-edge: #d9dddd;
    --bar: #1a1b1b;
    --bar-text: #ffffff;
    --brand-ink: #1f1f1f;
    --brand-green: #8fdc2c;
  }
  html, body {
    margin: 0;
    padding: 0;
    overflow: hidden;
    background: var(--bg-edge);
  }
  .card {
    position: relative;
    width: 1200px;
    height: 720px;
    overflow: hidden;
    background: radial-gradient(ellipse at 45% 40%, var(--bg-centre) 0%, #eceeee 45%, var(--bg-edge) 100%);
    font-family: "Arimo", Arial, sans-serif;
    color: var(--bar-text);
  }
  .brand {
    position: absolute;
    left: 70px;
    top: 300px;
    width: 320px;
    display: flex;
    align-items: center;
    gap: 18px;
  }
  .brand-name {
    color: var(--brand-ink);
    font-weight: 700;
    font-size: 50px;
    line-height: 1.05;
  }
  .brand-dot {
    width: 40px;
    height: 40px;
    flex: none;
    border-radius: 50%;
    background: var(--brand-green);
  }
  .bar {
    position: absolute;
    background: var(--bar);
    display: flex;
    align-items: center;
    box-sizing: border-box;
    white-space: nowrap;
    transform-origin: left center;
  }
  .bar-name {
    left: 405px; top: 102px; width: 461px; height: 98px;
    padding-left: 22px;
    font-size: 46px;
  }
  .bar-contact {
    left: 405px;
    padding-left: 88px;
    font-size: 35px;
    gap: 32px;
  }
  .bar-phone { top: 240px; width: 515px; height: 60px; transform: rotate(1deg); }
  .bar-email { top: 310px; width: 576px; height: 80px; transform: rotate(2.5deg); }
  .bar-web   { top: 396px; width: 462px; height: 66px; transform: rotate(2.5deg); }
  .contact-icon { width: 36px; height: 36px; flex: none; }
  .bar-title {
    left: 397px; top: 520px; width: 664px; height: 118px;
    padding-left: 34px;
    font-size: 48px;
    transform: rotate(-2.5deg);
  }
</style>
</head>
<body>
<main class="card">
  <div class="brand">
    <span class="brand-name">Pawsome<br>Trails</span>
    <span class="brand-dot" aria-hidden="true"></span>
  </div>

  <div class="bar bar-name">Marla Quinby, CTE</div>

  <div class="bar bar-contact bar-phone">
    <svg class="contact-icon" viewBox="0 0 36 36" aria-hidden="true">
      <rect x="10" y="6" width="16" height="28" rx="2" fill="none" stroke="#fff" stroke-width="2.5"/>
      <line x1="13" y1="1" x2="13" y2="6" stroke="#fff" stroke-width="2.5"/>
      <rect x="13" y="10" width="10" height="7" fill="#fff"/>
      <g fill="#fff">
        <rect x="13" y="20" width="3" height="2.5"/><rect x="16.5" y="20" width="3" height="2.5"/><rect x="20" y="20" width="3" height="2.5"/>
        <rect x="13" y="24" width="3" height="2.5"/><rect x="16.5" y="24" width="3" height="2.5"/><rect x="20" y="24" width="3" height="2.5"/>
        <rect x="13" y="28" width="3" height="2.5"/><rect x="16.5" y="28" width="3" height="2.5"/><rect x="20" y="28" width="3" height="2.5"/>
      </g>
    </svg>
    <span>647-555-0183</span>
  </div>

  <div class="bar bar-contact bar-email">
    <svg class="contact-icon" viewBox="0 0 36 36" aria-hidden="true">
      <path d="M4 16 L18 6 L32 16 V30 H4 Z" fill="none" stroke="#fff" stroke-width="2.5" stroke-linejoin="round"/>
      <path d="M4 16 L18 25 L32 16" fill="none" stroke="#fff" stroke-width="2.5" stroke-linejoin="round"/>
    </svg>
    <span>marla@pawsometrails.ca</span>
  </div>

  <div class="bar bar-contact bar-web">
    <svg class="contact-icon" viewBox="0 0 36 36" aria-hidden="true">
      <g fill="none" stroke="#fff" stroke-width="2">
        <circle cx="18" cy="18" r="14"/>
        <ellipse cx="18" cy="18" rx="6" ry="14"/>
        <line x1="18" y1="4" x2="18" y2="32"/>
        <line x1="4" y1="18" x2="32" y2="18"/>
        <path d="M7 10 H29 M7 26 H29"/>
      </g>
    </svg>
    <span>pawsometrails.ca</span>
  </div>

  <div class="bar bar-title">Certified Trainer Educator</div>
</main>
</body>
</html>
```